Brixelo Photography Business Cards

We need a good general business card that we can hand to our clients. We will be doing embossed gloss cards.

Target Market(s)

Real estate / Business to business / professionals

```html
<!DOCTYPE html>
<html lang="en">
<head>
<meta charset="utf-8">
<title>Brixelo Photography – Business Card</title>
<link rel="stylesheet" href="https://fonts.googleapis.com/css2?family=Montserrat:wght@400;500;600&display=swap">
<style>
  :root {
    --page-bg: #e4e5e9;
    --card-light: #f3f4f6;
    --navy: #2d2a7c;
    --roof-blue: #3b9fdc;
    --title-blue: #2f9bd8;
    --white: #ffffff;
    --rule: rgba(255, 255, 255, 0.45);
  }
  * { box-sizing: border-box; margin: 0; padding: 0; }
  html, body {
    width: 1200px; height: 1200px; overflow: hidden;
    background: var(--page-bg);
    font-family: "Montserrat", sans-serif;
  }
  .card {
    position: absolute; left: 70px; top: 306px;
    width: 1060px; height: 588px;
    background: var(--card-light);
    box-shadow: 0 18px 40px rgba(0,0,0,0.18);
    overflow: hidden;
  }
  .card-shapes { position: absolute; inset: 0; }
  .identity { position: absolute; left: 80px; top: 66px; }
  .identity-name {
    font-size: 37px; font-weight: 500; color: var(--navy); letter-spacing: 0.2px;
  }
  .identity-title {
    margin-top: 4px; font-size: 28px; font-weight: 400; color: var(--title-blue);
  }
  .contacts {
    position: absolute; left: 76px; top: 390px; width: 472px; list-style: none;
  }
  .contact-row {
    display: flex; align-items: center; gap: 16px;
    height: 48px; color: var(--white); font-size: 24px; font-weight: 400;
    border-bottom: 1.5px solid var(--rule);
    white-space: nowrap;
  }
  .contact-row:last-child { border-bottom: none; }
  .contact-icon { width: 22px; height: 22px; flex: none; }
  .brand-seal {
    position: absolute; left: 552px; top: 68px;
    width: 440px; height: 440px; border-radius: 50%;
    background: var(--white);
    display: flex; flex-direction: column; align-items: center; justify-content: center;
    text-align: center; color: var(--navy);
    font-weight: 600; line-height: 1.15;
  }
  .brand-seal .brand-word { font-size: 62px; }
  .brand-seal .brand-sub { font-size: 40px; }
</style>
</head>
<body>
  <div class="card">
    <svg class="card-shapes" width="1060" height="588" viewBox="0 0 1060 588">
      <path d="M44 120 V40 H88" fill="none" stroke="var(--navy)" stroke-width="4"/>
      <path d="M0 336 H150 L229 282 L308 336 H1060 V588 H0 Z" fill="var(--navy)"/>
      <path d="M0 326 H146 L229 268 L312 326 H1060" fill="none" stroke="var(--roof-blue)" stroke-width="5"/>
    </svg>

    <div class="identity">
      <p class="identity-name">Marcus Delaney</p>
      <p class="identity-title">Photographer</p>
    </div>

    <ul class="contacts">
      <li class="contact-row">
        <svg class="contact-icon" viewBox="0 0 24 24" fill="none" stroke="var(--white)" stroke-width="2"><path d="M5 3h4l2 5-3 2a11 11 0 0 0 6 6l2-3 5 2v4a2 2 0 0 1-2 2A17 17 0 0 1 3 5a2 2 0 0 1 2-2z"/></svg>
        <span>360.555.0148</span>
      </li>
      <li class="contact-row">
        <svg class="contact-icon" viewBox="0 0 24 24" fill="var(--white)"><rect x="2" y="5" width="20" height="14" rx="1"/><path d="M3 6l9 7 9-7" fill="none" stroke="var(--navy)" stroke-width="1.8"/></svg>
        <span>info@brixelophoto.com</span>
      </li>
      <li class="contact-row">
        <svg class="contact-icon" viewBox="0 0 24 24" fill="none" stroke="var(--white)" stroke-width="1.8"><circle cx="12" cy="12" r="10"/><ellipse cx="12" cy="12" rx="4.5" ry="10"/><path d="M2 12h20"/></svg>
        <span>www.brixelophoto.com</span>
      </li>
    </ul>

    <div class="brand-seal">
      <span class="brand-word">Brixelo</span>
      <span class="brand-sub">Photography</span>
    </div>
  </div>
</body>
</html>
```